Atelier Vane Architecture business card

We need to update our business card. We do high end custom residential, hospitality, and wellness architecture. We focus on creating unique spaces and design around the five senses, believing that architecture's true impact is not on our surroundings, but within us. We would like to see designs are instill a sense of calm awe. They should be crisp, fresh, clean, authentic, & contemporary without being sterile, overworked, or harsh. White space is important. Alternative materials are an option if natural. We have created our own logo and would like designs to incorporate it. However, we are willing to see alternatives if the logo becomes a stumbling block and you have an alternate you suggest. Card must have the following information:
Atelier Vane Architecture, Inc.
742 Marbury Rd. NE Atlanta, GA 30319
Dominic K. Whitlow, AIA, NCARB, LEED AP BD+C
ateliervane.example

Target Market(s)

Higher net worth individuals with an appreciation for design, nature, sustainability,

Industry/Entity Type

Architect

Contact Information for Business Card

See above. The title of Owner or Architect is helpful but not necessary. Minimalism should trump additional information.

Font styles to use
Serif
Sans Serif

Requirements
Must have
• It should look professional. It must use logo
Should not have
• caligraphy, animals, anything that is cute,

```html
<!DOCTYPE html>
<html lang="en">
<head>
<meta charset="utf-8">
<title>Atelier Vane Architecture — Business Card</title>
<link rel="stylesheet" href="https://fonts.googleapis.com/css2?family=Hind:wght@400;600&display=swap">
<style>
  :root {
    --backdrop: #5b4b3d;
    --charcoal: #464646;
    --paper: #ffffff;
    --forest: #005742;
    --ink-light: #ffffff;
    --ink-mid: #4a4a4a;
  }
  * { margin: 0; padding: 0; box-sizing: border-box; }
  html, body {
    width: 1200px;
    height: 987px;
    overflow: hidden;
    background: var(--backdrop);
    font-family: "Hind", Arial, sans-serif;
  }
  .canvas {
    position: relative;
    width: 1200px;
    height: 987px;
  }
  .card {
    position: absolute;
    left: 292px;
    width: 616px;
    height: 352px;
    box-shadow: 0 2px 6px rgba(0,0,0,0.45);
    overflow: hidden;
  }
  .card--front { top: 130px; background: var(--paper); }
  .card--back  { top: 506px; background: var(--forest); }

  .contact-band {
    height: 153px;
    background: var(--charcoal);
    color: var(--ink-light);
    text-align: center;
    padding-top: 22px;
  }
  .contact-band__name {
    font-weight: 600;
    font-size: 23px;
    letter-spacing: 0.5px;
    line-height: 1.2;
  }
  .contact-band__credentials {
    font-weight: 400;
    font-size: 14px;
    line-height: 1.3;
    margin-top: 1px;
  }
  .contact-band__address {
    font-size: 16px;
    margin-top: 12px;
    line-height: 1.3;
  }
  .contact-band__web {
    font-size: 16px;
    letter-spacing: 1px;
    margin-top: 8px;
    line-height: 1.3;
  }

  .brand-area {
    position: absolute;
    left: 0; right: 0;
    top: 153px;
    height: 185px;
    display: flex;
    align-items: center;
    justify-content: center;
  }
  .card--back .brand-area { top: 0; height: 352px; }

  .wordmark {
    font-weight: 400;
    font-size: 27px;
    letter-spacing: 6px;
    text-transform: uppercase;
    color: var(--ink-mid);
    line-height: 1;
    text-align: center;
  }
  .card--back .wordmark { color: var(--ink-light); }

  .accent-strip {
    position: absolute;
    left: 0; right: 0; bottom: 0;
    height: 14px;
    background: var(--forest);
  }
</style>
</head>
<body>
<main class="canvas">
  <section class="card card--front" aria-label="Business card front">
    <header class="contact-band">
      <p class="contact-band__name">DOMINIC K. WHITLOW</p>
      <p class="contact-band__credentials">AIA, NCARB, LEED AP BD+C</p>
      <p class="contact-band__address">742 MARBURY RD. NE ATLANTA, GA 30319</p>
      <p class="contact-band__web">WWW.ATELIERVANE.EXAMPLE</p>
    </header>
    <div class="brand-area">
      <p class="wordmark">Atelier Vane Architecture</p>
    </div>
    <div class="accent-strip"></div>
  </section>

  <section class="card card--back" aria-label="Business card back">
    <div class="brand-area">
      <p class="wordmark">Atelier Vane Architecture</p>
    </div>
  </section>
</main>
</body>
</html>
```